Banner Ad Design Project: Image banner for new website

Hi,

we need an image banner for a new website we just launched. The image banner should come in the formats 728x90 and 300x250.

The website the banner should advertise is http://www.vellora-tonebox.com/ .

We leave it up to your experience to find the best text and to obtain a great clickrate. Banner should be CATCHY and MOTIVATE people to enter. We do not want to include our current "logo". Will require all design files and fonts.

Best regards,
Brendan

```html
<!DOCTYPE html>
<html lang="en">
<head>
<meta charset="utf-8">
<title>Listen Online to Relaxing Sounds</title>
<link href="https://fonts.googleapis.com/css2?family=Arimo:wght@700&family=Delius&display=swap" rel="stylesheet">
<style>
  :root {
    --sky-top: #9fd3f2;
    --sky-mid: #d4ecfa;
    --sky-low: #f4fafe;
    --blue-light: #1f9ce0;
    --blue-dark: #0b5fae;
    --green-script: #6ea23a;
    --leaf-dark: #3f9a1e;
    --leaf-light: #a6dc4c;
    --button-top: #d9f07a;
    --button-bottom: #8cc63a;
    --button-text: #2f5d12;
    --photo-tone-a: #dfe8ee;
    --photo-tone-b: #c9a58e;
    --photo-tone-c: #3a3a3e;
  }
  * { margin: 0; padding: 0; box-sizing: border-box; }
  html, body { width: 1200px; height: 148px; overflow: hidden; background: #ffffff; }
  .banner {
    position: relative;
    width: 1200px;
    height: 148px;
    overflow: hidden;
    background: linear-gradient(180deg, var(--sky-top) 0%, var(--sky-mid) 45%, var(--sky-low) 100%);
    border: 1px solid #c6dbe8;
  }
  .leaves-art {
    position: absolute;
    left: 0; top: 0;
    width: 315px; height: 148px;
    background:
      radial-gradient(ellipse 150px 40px at 140px 40px, var(--leaf-light) 0%, var(--leaf-dark) 70%, transparent 72%),
      radial-gradient(ellipse 120px 34px at 70px 95px, var(--leaf-dark) 0%, var(--leaf-light) 65%, transparent 68%),
      linear-gradient(90deg, rgba(120,190,60,.35), transparent);
  }
  .headline {
    position: absolute;
    left: 318px; top: 10px;
    font-family: "Arimo", Arial, sans-serif;
    font-weight: 700;
    font-size: 72px;
    line-height: 1;
    letter-spacing: -3px;
    white-space: nowrap;
  }
  .headline .listen { color: var(--blue-light); }
  .headline .online { color: var(--blue-dark); }
  .tagline {
    position: absolute;
    left: 330px; top: 82px;
    font-family: "Delius", "Comic Sans MS", cursive;
    font-size: 48px;
    line-height: 1;
    white-space: nowrap;
    color: var(--green-script);
  }
  .tagline .to { color: var(--blue-dark); }
  .listener-photo {
    position: absolute;
    right: 0; top: 0;
    width: 300px; height: 148px;
    background: linear-gradient(100deg, rgba(223,232,238,0) 0%, var(--photo-tone-a) 20%, var(--photo-tone-b) 55%, var(--photo-tone-c) 100%);
  }
  .play-button {
    position: absolute;
    left: 933px; top: 102px;
    width: 174px; height: 36px;
    border-radius: 18px;
    background: linear-gradient(180deg, var(--button-top), var(--button-bottom));
    border: 1px solid #7aae2e;
    display: flex;
    align-items: center;
    justify-content: space-between;
    padding: 0 6px 0 18px;
    font-family: "Arimo", Arial, sans-serif;
    font-weight: 700;
    font-size: 19px;
    color: var(--button-text);
    text-decoration: none;
    box-shadow: 0 2px 3px rgba(0,0,0,.25);
  }
  .play-button svg { width: 28px; height: 28px; }
</style>
</head>
<body>
  <div class="banner">
    <div class="leaves-art" role="img" aria-label="Green leaves with water droplets and a small ladybug"></div>

    <h1 class="headline"><span class="listen">LISTEN</span> <span class="online">ONLINE</span></h1>
    <p class="tagline"><span class="to">to</span> Relaxing Sounds</p>

    <div class="listener-photo" role="img" aria-label="Photo of a relaxed woman listening with headphones"></div>

    <a class="play-button" href="http://www.vellora-tonebox.com/">
      PLAY NOW
      <svg viewBox="0 0 28 28" aria-hidden="true">
        <circle cx="14" cy="14" r="12" fill="#ffffff" stroke="#9ccc4a" stroke-width="1.5"/>
        <path d="M7 11.5h3l4-3.5v12l-4-3.5H7z" fill="#4d7f1e"/>
        <path d="M16.5 11a4 4 0 0 1 0 6M18.5 9a7 7 0 0 1 0 10" fill="none" stroke="#4d7f1e" stroke-width="1.5" stroke-linecap="round"/>
      </svg>
    </a>
  </div>
</body>
</html>
```